Zestora - The Natural Energydrink
Zielgruppe
Wir sind eine Imkerei und unsere Zielgruppe ist der Moderne verbraucher der auf die umwelt achtet und sich bewusst ernähren möchte. Zielgruppe ist von 16-33 Jahren ca.
Aufgabenstellung
Es geht um Zestora, ein Natural Energydrink der in einer 0,33l Limonadenflasche abgefüllt werden soll und nicht in eine Dose, das ist auch schon der gedanke hinter dem Produkt. Natürlichkeit, Umweltbewusstsein, Ökologisch. Der Energydrink, der ausschließlich mit Honig gesüßt ist und nicht mit Industriellen Zucker. Das Etikett für den Natural Energydrink soll Modern sein aber auch die 'Ältere' zielgruppe ansprechen. Gewünscht ist ein Front, Rücken und Hals Etikett für die Flasche die auch gut zusammen passen. Rücken ist dann natürlich fast nur inhaltstoffe und hersteller und eben diese Pflichtangaben.
Das Thema Biene und Honig sollte sich natürlich wiederfinden und das Design sollte in Gelb schwarz gehalten sein. Auch Wabenmuster machen sich gut. Nicht zu 'lieb' es ist immerhin noch ein energy drink aber auch nicht zu 'Hart' es soll auch die naturverliebten 'Ökos' ansprechen. Schwieriger Spagat zwischen Öko und Energydrink in berücksichtigung der Honig Thematik.
Maße können die klassischen 0,33l Etikettenmaße sein, müssen sie aber nicht.
Front: 9cm hoch und 8,5cm breit
Halsetikett: 6cm hoch und 9cm breit mit Überlappung
Rücken Etikett: 8cm hoch und 6cm breit
Größe und Form sind aber nicht vorgegeben. Es sollte am schluss harmonisch sein und gut und übersichtlich alle Informationen griffbereit sein für den verbraucher.
Pflichtangaben auf dem Rückenetikett sind:
die Zutaten auflistung und die klassische Tabelle auf 100ml und auf 0,33ml ( Zucker, Kcal usw.) Es sollte ein EAN Code mit eingebunden werden und solche dinge wie ein Facebook und Instagram Symbol machen sich auch immer gut. Weiterhin der Textblock: 'Kohlensäurehaltig, Koffeinhaltig, kühl und trocken lagern. Für Kinder, Diabetiker, schwangere Frauen und koffeinempfindliche Personen nicht geeignet. Nur in Begrensten Mengen Konsumieren.'
Darüber hinaus muss natürlich der sehr werbewirksame Slogan ' Made in Germany' dazu ;)

```html
<!DOCTYPE html>
<html lang="de">
<head>
<meta charset="utf-8">
<title>Zestora - The Natural Energydrink</title>
<link rel="stylesheet" href="https://fonts.googleapis.com/css2?family=Fredoka:wght@700&family=Open+Sans:wght@300&display=swap">
<style>
  :root {
    --frame: #1b1b28;
    --honey-light: #fde45a;
    --honey: #fcd11e;
    --honey-deep: #f3b800;
    --panel: #000000;
    --edge: #ffffff;
    --gold: #f7c600;
    --gold-dim: #3d3100;
  }
  html, body {
    margin: 0;
    padding: 0;
    overflow: hidden;
    background: #ffffff;
  }
  .label {
    position: relative;
    width: 928px;
    height: 1200px;
    box-sizing: border-box;
    border: 12px solid var(--frame);
    overflow: hidden;
  }
  .comb-field {
    position: absolute;
    inset: 0;
    background: radial-gradient(ellipse at 50% 45%, var(--honey-light) 0%, var(--honey) 55%, var(--honey-deep) 100%);
  }
  .emblem {
    position: absolute;
    left: -12px;
    top: -12px;
    width: 928px;
    height: 1200px;
  }
  .bee-mark {
    position: absolute;
    left: 410px;
    top: 267px;
    width: 130px;
    height: 162px;
    border-radius: 40%;
    background: var(--gold-dim);
  }
  .brand-name {
    position: absolute;
    left: -12px;
    width: 928px;
    top: 506px;
    margin: 0;
    text-align: center;
    font-family: "Fredoka", sans-serif;
    font-weight: 700;
    font-size: 148px;
    line-height: 1;
    letter-spacing: 3px;
    color: var(--gold);
  }
  .tagline {
    position: absolute;
    left: -12px;
    width: 928px;
    top: 699px;
    margin: 0;
    text-align: center;
    font-family: "Open Sans", sans-serif;
    font-weight: 300;
    font-size: 39px;
    line-height: 1;
    letter-spacing: -0.5px;
    color: var(--gold);
  }
</style>
</head>
<body>
  <div class="label">
    <div class="comb-field" role="img" aria-label="Honigfarbenes Wabenmuster als Hintergrund"></div>

    <svg class="emblem" viewBox="0 0 928 1200" aria-hidden="true">
      <polygon points="463,138 866,369 866,823 463,1054 60,823 60,369" fill="var(--edge)"/>
      <polygon points="463,147 858,374 858,818 463,1045 68,818 68,374" fill="var(--panel)"/>
      <polygon points="463,174 830,386 830,806 463,1018 96,806 96,386" fill="none" stroke="var(--gold)" stroke-width="3"/>
      <line x1="166" y1="504" x2="762" y2="504" stroke="var(--gold)" stroke-width="2"/>
      <line x1="166" y1="685" x2="762" y2="685" stroke="var(--gold)" stroke-width="2"/>
    </svg>

    <div class="bee-mark" role="img" aria-label="Goldene Bienen-Illustration in Linienoptik"></div>

    <h1 class="brand-name">ZESTORA</h1>
    <p class="tagline">THE NATURAL ENERGYDRINK</p>
  </div>
</body>
</html>
```